Kindro - Bringing Warmth and Quality to Senior Living

We are a new company based in Sydney, Australia. We have developed a state-of-the-art app for communication between aged care facilities and families.

Kindro has been developed for facilities to augment the best possible care by providing easy, safe and secure communication for families to stay in touch with their loved ones.
Updates

the website needs to be designed so we can add functionality including multilingual support. display in different languages.we also require enquiry and email/data base function. we want it simple and clean so its responsive. the target audience will be 40+ in age. there will be a video on home page. would like to start with 6 pages/ subjects -homepage -about us -our solution -demonstration page, this will be a page that contains videos of people using our product -customer testimonials -contact us

Target Market(s)

Aged care facilities.
Families (over 40’s age group) who are looking for a facility for their loved ones.

Number of Pages Required

5+ page

Font styles to use
Sans Serif

Colors
faa54b
ffffff
0255a3

Requirements
Must have
• - Our corporate colour is #EE8811.
• - If you're using stock photography, please use brimlo prints photos as we have a license for their photos.
• - The design needs to be responsive (mobile and desktop)
• -White space on each page
Nice to have
• -need to leave a place for a future animation video to be added in on the home tab
Should not have
• we don't want flash technology

```html
<!DOCTYPE html>
<html lang="en">
<head>
<meta charset="utf-8">
<title>Kindro - Bringing Warmth and Quality to Senior Living</title>
<link href="https://fonts.googleapis.com/css2?family=Montserrat:wght@400;500;600;700;800&display=swap" rel="stylesheet">
<style>
:root{
  --orange:#f47b20;
  --orange-soft:#faa54b;
  --dark:#3e4345;
  --dark-2:#555b5d;
  --text:#333;
  --muted:#555;
  --line:#e3e3e3;
  --nav:#f3f3f3;
  --white:#fff;
}
*{box-sizing:border-box;margin:0;padding:0}
html,body{width:1200px;height:4484px;overflow:hidden}
body{position:relative;font-family:'Montserrat',sans-serif;color:var(--text);background:var(--white)}
.abs{position:absolute}
.topbar{left:0;top:0;width:1200px;height:42px;background:var(--orange);color:#fff;font-size:14px}
.topbar .dots{left:112px;top:15px;display:flex;gap:13px}
.topbar .dots span{width:11px;height:11px;border-radius:50%;background:#fff;display:block}
.topbar .addr{right:100px;top:12px}
.topbar .sep{left:318px;top:0;width:1px;height:42px;background:rgba(255,255,255,.5)}
.topbar .sep2{left:853px}
.header{left:0;top:42px;width:1200px;height:111px;background:#fff}
.search{left:134px;top:33px;width:247px;height:43px;border:1px solid #ddd;border-radius:22px;font-size:13px;color:#777;padding:12px 16px}
.search i{position:absolute;right:4px;top:5px;width:32px;height:32px;border-radius:50%;background:var(--orange)}
.search i:after{content:"";position:absolute;left:10px;top:9px;width:9px;height:9px;border:2px solid #fff;border-radius:50%}
.brand{left:452px;top:20px;display:flex;align-items:center;gap:14px}
.brand b{width:62px;height:62px;border-radius:50%;background:var(--orange);display:block}
.brand span{font-size:58px;font-weight:600;color:var(--orange);letter-spacing:1px}
.call{left:914px;top:30px;display:flex;gap:14px;align-items:center}
.call .txt{font-size:16px;line-height:24px}
.call .txt strong{color:var(--orange);font-weight:600;display:block}
.nav{left:0;top:153px;width:1200px;height:63px;background:var(--nav);border-top:1px solid var(--line);border-bottom:1px solid var(--line);display:flex;justify-content:center;gap:44px;align-items:center;font-size:18px;font-weight:500}
.hero{left:0;top:216px;width:1200px;height:650px;background:linear-gradient(120deg,#d8d2cb,#ece8e3 45%,#c9bfb4)}
.hero-title{left:693px;top:350px;font-size:96px;font-weight:600;color:var(--orange);line-height:1}
.hero-sub{left:700px;top:468px;font-size:23px;font-weight:600;line-height:46px;color:#2a2a2a}
.btn{display:flex;align-items:center;justify-content:center;gap:8px;background:var(--orange);color:#fff;font-weight:600;font-size:18px}
.btn:after{content:"›";width:16px;height:16px;border-radius:50%;background:#fff;color:var(--orange);font-size:15px;line-height:14px;text-align:center;font-weight:800}
.photo-circle{border-radius:50%;overflow:hidden}
.ring{border-radius:50%;border:5px solid var(--orange);border-left-color:transparent;border-bottom-color:transparent;transform:rotate(-10deg)}
.section-title{font-size:38px;font-weight:700;color:var(--orange);line-height:1}
.para{font-size:16px;line-height:31.3px;text-align:justify;color:var(--muted)}
.dark-band{background:var(--dark)}
.on-dark{color:#eee}
.testimonial{left:160px;top:3082px;width:880px;text-align:center;color:#eee;font-size:19px;line-height:36px}
.quote{left:0;top:3028px;width:1200px;text-align:center;font-size:110px;line-height:1;font-weight:800;color:#fff;height:60px;overflow:hidden}
.name{left:0;top:3205px;width:1200px;text-align:center;font-size:23px;font-weight:600;color:#fff}
.field{height:40px;border:1px solid var(--line);box-shadow:inset 0 1px 3px rgba(0,0,0,.06);font-size:11px;color:#555;padding:13px 18px}
.submit{left:510px;top:3794px;width:180px;height:47px;background:var(--orange);color:#fff;font-weight:700;font-size:18px;display:flex;align-items:center;justify-content:center}
.foot-icon{width:84px;height:84px;border-radius:50%;background:var(--orange)}
.foot-text{width:300px;text-align:center;color:#eee;font-size:19px;line-height:29px}
.foot-links{left:0;top:4338px;width:1200px;text-align:center;color:#fff;font-size:17px;font-weight:500}
.copy{left:0;top:4384px;width:1200px;text-align:center;color:#ddd;font-size:15px}
.socials{left:530px;top:4424px;display:flex;gap:8px}
.socials span{width:30px;height:30px;border:2px solid #fff;border-radius:50%;display:block}
</style>
</head>
<body>

<div class="abs topbar">
  <div class="abs dots"><span></span><span></span><span></span><span></span><span></span><span></span><span></span></div>
  <div class="abs sep"></div><div class="abs sep sep2"></div>
  <div class="abs addr">14 Marlow Lane, Dunmore, NSW 2529</div>
</div>

<header class="abs header">
  <div class="abs search">Search<i></i></div>
  <div class="abs brand"><b></b><span>Kindro</span></div>
  <div class="abs call">
    <svg width="42" height="42" viewBox="0 0 42 42"><circle cx="21" cy="21" r="19" fill="none" stroke="#f47b20" stroke-width="3"/><path d="M14 12c2-1 3 0 4 3l-2 2c1 3 3 5 6 6l2-2c3 1 4 2 3 4-1 2-3 3-5 2-6-2-10-6-11-11 0-2 1-3 3-4z" fill="#f47b20"/></svg>
    <div class="txt"><strong>Call us:</strong>555 010 2040</div>
  </div>
</header>

<nav class="abs nav"><span>Home</span><span>About Us</span><span>Our Solution</span><span>Customer Testimonials</span><span>Our Team</span><span>Contact Us</span></nav>

<div class="abs hero" role="img" aria-label="Photo of a carer gently embracing a smiling senior woman in a bright room"></div>
<svg class="abs" style="left:0;top:740px" width="1200" height="260" viewBox="0 0 1200 260">
  <path d="M0 126 C200 110 420 20 640 28 C860 38 1060 150 1200 253 L1200 260 L0 260Z" fill="#f47b20"/>
  <path d="M0 132 C220 115 420 45 630 48 C860 55 1040 150 1200 250 L1200 260 L0 260Z" fill="#fff"/>
  <path d="M0 132 C200 130 420 65 620 62 C860 60 1050 170 1200 260 L0 260Z" fill="#fff"/>
</svg>
<div class="abs hero-title">Kindro</div>
<div class="abs hero-sub">Sed ut perspiciatis unde omnis iste<br>natus error voluptatem</div>
<div class="abs btn" style="left:700px;top:570px;width:159px;height:48px">Read More</div>

<!-- About -->
<div class="abs ring" style="left:85px;top:994px;width:450px;height:450px"></div>
<div class="abs photo-circle" role="img" aria-label="Video thumbnail: two women sharing tea on a sofa" style="left:98px;top:1019px;width:420px;height:420px;background:linear-gradient(135deg,#d9d5cf,#bfb5aa 60%,#8e8a8a)"></div>
<svg class="abs" style="left:278px;top:1195px" width="56" height="60" viewBox="0 0 56 60"><path d="M0 0 L56 30 L0 60Z" fill="#f47b20"/></svg>
<h2 class="abs section-title" style="left:578px;top:1060px">ABOUT US</h2>
<p class="abs para" style="left:578px;top:1112px;width:535px">Sed ut perspiciatis unde omnis iste natus error sit voluptatem accusantium doloremque laudantium, totam rem aperiam, eaque ipsa quae ab illo inventore veritatis et quasi architecto beatae vitae dicta sunt explicabo. Nemo enim ipsam voluptatem quia voluptas sit aspernatur aut odit aut fugit, sed quia consequuntur magni dolores eos qui ratione voluptatem sequi nesciunt.</p>
<div class="abs btn" style="left:578px;top:1320px;width:159px;height:47px">Read More</div>

<!-- Our Solution -->
<div class="abs dark-band" role="img" aria-label="Muted background photo of a carer with a senior resident" style="left:0;top:1515px;width:1200px;height:697px;background:linear-gradient(90deg,#3b4042,#4a5052 60%,#3e4345)"></div>
<svg class="abs" style="left:0;top:1505px" width="1200" height="60" viewBox="0 0 1200 60">
  <path d="M0 0 H1200 V25 C900 60 600 5 300 22 C180 28 80 30 0 28Z" fill="#fff"/>
  <path d="M0 8 C120 5 250 25 420 24 C700 20 900 55 1200 28 L1200 22 C900 50 700 12 420 14 C250 16 120 0 0 0Z" fill="#f47b20"/>
</svg>
<svg class="abs" style="left:0;top:2150px" width="1200" height="70" viewBox="0 0 1200 70">
  <path d="M0 40 C300 10 700 70 1200 40 L1200 70 L0 70Z" fill="#fff"/>
  <path d="M500 48 C750 60 1000 55 1200 36 L1200 60 C1000 70 760 66 500 48Z" fill="#f47b20"/>
</svg>
<h2 class="abs section-title" style="left:90px;top:1703px">OUR SOLUTION</h2>
<p class="abs para on-dark" style="left:90px;top:1756px;width:535px">Sed ut perspiciatis unde omnis iste natus error sit voluptatem accusantium doloremque laudantium, totam rem aperiam, eaque ipsa quae ab illo inventore veritatis et quasi architecto beatae vitae dicta sunt explicabo. Nemo enim ipsam voluptatem quia voluptas sit aspernatur aut odit aut fugit, sed quia consequuntur magni dolores eos qui ratione voluptatem sequi nesciunt.</p>
<div class="abs btn" style="left:90px;top:1963px;width:159px;height:47px">Read More</div>
<div class="abs" style="left:677px;top:1649px;width:446px;height:446px;border-radius:50%;background:var(--orange);border:6px solid #1e1e1e;border-left-color:var(--orange)"></div>
<div class="abs" role="img" aria-label="Hand holding a smartphone showing the app start screen" style="left:782px;top:1588px;width:230px;height:452px;border-radius:34px;background:linear-gradient(#2a2a2a,#111);padding:12px">
  <div style="width:100%;height:100%;border-radius:24px;background:#fff;display:flex;align-items:center;justify-content:center;font-size:50px;font-weight:600;color:var(--orange)">Kindro</div>
</div>

<!-- Demonstration -->
<div class="abs ring" style="left:85px;top:2266px;width:450px;height:450px"></div>
<div class="abs photo-circle" role="img" aria-label="Carer chatting with a senior woman in a wheelchair" style="left:98px;top:2291px;width:420px;height:420px;background:linear-gradient(135deg,#e2ded8,#c7bdb0 55%,#8f9a86)"></div>
<h2 class="abs section-title" style="left:578px;top:2333px">DEMONSTRATION</h2>
<p class="abs para" style="left:578px;top:2385px;width:535px">Sed ut perspiciatis unde omnis iste natus error sit voluptatem accusantium doloremque laudantium, totam rem aperiam, eaque ipsa quae ab illo inventore veritatis et quasi architecto beatae vitae dicta sunt explicabo. Nemo enim ipsam voluptatem quia voluptas sit aspernatur aut odit aut fugit, sed quia consequuntur magni dolores eos qui ratione voluptatem sequi nesciunt.</p>
<div class="abs btn" style="left:578px;top:2594px;width:159px;height:47px">Read More</div>

<!-- Testimonials -->
<div class="abs dark-band" role="img" aria-label="Muted background photo of a smiling senior couple" style="left:0;top:2778px;width:1200px;height:627px;background:linear-gradient(90deg,#3e4345,#555b5c 50%,#3e4345)"></div>
<svg class="abs" style="left:0;top:2770px" width="1200" height="60" viewBox="0 0 1200 60">
  <path d="M0 0 H1200 V10 C900 20 500 15 0 40Z" fill="#fff"/>
  <path d="M600 20 C850 8 1050 5 1200 8 L1200 22 C1000 22 800 25 600 20Z" fill="#f47b20"/>
</svg>
<svg class="abs" style="left:0;top:3345px" width="1200" height="65" viewBox="0 0 1200 65">
  <path d="M0 55 C300 70 700 10 1200 28 L1200 65 L0 65Z" fill="#fff"/>
  <path d="M0 50 C150 55 300 52 450 44 C300 58 150 62 0 60Z" fill="#f47b20"/>
</svg>
<h2 class="abs section-title" style="left:0;top:2964px;width:1200px;text-align:center">TESTIMONIALS</h2>
<div class="abs quote">&ldquo;</div>
<p class="abs testimonial">Sed ut perspiciatis unde omnis iste natus error sit voluptatem accusantium doloremque laudantium, totam rem aperiam, eaque ipsa quae ab illo inventore veritatis et quasi architecto beatae vitae dicta sunt explicabo.</p>
<div class="abs name">Margaret Hale</div>
<svg class="abs" style="left:64px;top:3086px" width="68" height="40" viewBox="0 0 68 40"><path d="M66 20 H4 M22 3 L4 20 L22 37" fill="none" stroke="#fff" stroke-width="4"/></svg>
<svg class="abs" style="left:1064px;top:3086px" width="68" height="40" viewBox="0 0 68 40"><path d="M2 20 H64 M46 3 L64 20 L46 37" fill="none" stroke="#fff" stroke-width="4"/></svg>

<!-- Contact -->
<h2 class="abs section-title" style="left:0;top:3507px;width:1200px;text-align:center">CONTACT US</h2>
<div class="abs field" style="left:162px;top:3576px;width:428px">&#9679; First Name</div>
<div class="abs field" style="left:610px;top:3576px;width:430px">&#9679; Last Name</div>
<div class="abs field" style="left:162px;top:3630px;width:428px">&#9632; Address</div>
<div class="abs field" style="left:162px;top:3685px;width:428px">&#9633; Email Address</div>
<div class="abs field" style="left:162px;top:3740px;width:428px">&#9743; Phone Number</div>
<div class="abs field" style="left:610px;top:3630px;width:430px;height:150px">&#9679; Message :</div>
<div class="abs submit">SUBMIT</div>

<!-- Footer -->
<div class="abs dark-band" role="img" aria-label="Muted background photo of a carer and senior resident" style="left:0;top:3960px;width:1200px;height:524px;background:linear-gradient(90deg,#3e4345,#4d5355 50%,#3e4345)"></div>
<svg class="abs" style="left:0;top:3880px" width="1200" height="140" viewBox="0 0 1200 140">
  <path d="M0 0 C100 60 260 110 500 100 C800 88 1000 40 1200 70 L1200 140 L0 140Z" fill="#3e4345"/>
  <path d="M0 0 C120 80 300 115 520 100 C300 125 120 95 0 40Z" fill="#f47b20"/>
  <path d="M60 50 C220 95 380 100 560 85 C400 108 220 105 60 60Z" fill="#fff"/>
  <path d="M650 75 C850 45 1050 25 1200 40 L1200 55 C1050 42 850 58 650 75Z" fill="#f47b20"/>
</svg>
<div class="abs foot-icon" style="left:242px;top:4156px"></div>
<svg class="abs" style="left:266px;top:4176px" width="36" height="44" viewBox="0 0 36 44"><path d="M18 42 C6 28 4 22 4 16 A14 14 0 0 1 32 16 C32 22 30 28 18 42Z" fill="none" stroke="#fff" stroke-width="2.5"/><circle cx="18" cy="16" r="5" fill="none" stroke="#fff" stroke-width="2.5"/></svg>
<div class="abs foot-icon" style="left:547px;top:4156px"></div>
<svg class="abs" style="left:570px;top:4178px" width="40" height="40" viewBox="0 0 40 40"><path d="M9 4c3-1 5 1 6 5l-3 3c2 5 5 8 10 10l3-3c4 1 6 3 5 6-1 3-4 5-7 4C14 26 8 20 5 11 4 8 6 5 9 4z" fill="none" stroke="#fff" stroke-width="2.5"/></svg>
<div class="abs foot-icon" style="left:850px;top:4156px"></div>
<svg class="abs" style="left:872px;top:4182px" width="40" height="32" viewBox="0 0 40 32"><rect x="2" y="2" width="36" height="28" fill="none" stroke="#fff" stroke-width="2.5"/><path d="M2 2 L20 18 L38 2 M2 30 L15 15 M38 30 L25 15" fill="none" stroke="#fff" stroke-width="2.5"/></svg>
<div class="abs foot-text" style="left:134px;top:4250px">14 Marlow Lane,<br>Dunmore, NSW 2529</div>
<div class="abs foot-text" style="left:439px;top:4250px">Phone:<br>555 010 2041</div>
<div class="abs foot-text" style="left:742px;top:4250px">Email:<br>care@kindro.example</div>
<div class="abs foot-links">Home &nbsp;|&nbsp; About Us &nbsp;|&nbsp; Our Solution &nbsp;|&nbsp; Customer Testimonials &nbsp;|&nbsp; Our Team &nbsp;|&nbsp; Contact Us</div>
<div class="abs copy">© 2019 Kindro &nbsp;All right reserved</div>
<div class="abs socials"><span></span><span></span><span></span><span></span></div>

</body>
</html>
```